Cellar Guard Sealing
Business Cards
Project: Cellar Guard Sealing
Cellar Guard Sealing -
Creative Brief
Professional
Dorian Whitcombe
4826 Fernhill Glen Court #317 Gainesville, VA 20155
dwhitcombe@cellarguardsealing.example
www.cellarguardsealing.example
by line is : because it's not just any house...it's your home!
open to suggestions...be creative

```html
<!DOCTYPE html>
<html lang="en">
<head>
<meta charset="utf-8">
<title>Cellar Guard Sealing – Stationery Set</title>
<link rel="stylesheet" href="https://fonts.googleapis.com/css2?family=Arimo:wght@400;700&family=Tinos:wght@400;700&display=swap">
<style>
  :root{
    --stage:#a4a4a4;
    --paper:#ffffff;
    --brand-blue:#1f6db5;
    --brand-green:#3e9a47;
    --brand-navy:#1c3f78;
    --ink:#333333;
    --ink-soft:#666666;
    --signature-tone:#d9d9d9;
  }
  *{box-sizing:border-box;margin:0;padding:0}
  html,body{width:1200px;height:626px;overflow:hidden}
  body{background:var(--stage);position:relative;font-family:"Arimo",Arial,sans-serif;color:var(--ink)}

  .piece{position:absolute;background:var(--paper);box-shadow:0 1px 3px rgba(0,0,0,.25)}

  .brand-name{
    font-family:"Arimo",Arial,sans-serif;font-weight:700;color:var(--brand-navy);
    text-transform:uppercase;line-height:1.05;display:flex;align-items:center;gap:5px
  }
  .brand-dot{border-radius:50%;background:var(--brand-blue);flex:none}

  /* business card front */
  .card-front{left:7px;top:252px;width:149px;height:96px;display:flex;align-items:center;justify-content:center}
  .card-front .brand-name{font-size:10px;flex-direction:column;text-align:center}
  .card-front .brand-dot{width:16px;height:16px}

  /* business card back */
  .card-back{left:7px;top:360px;width:149px;height:127px;padding:10px 8px}
  .card-back .brand-name{font-size:8px}
  .card-back .brand-dot{width:11px;height:11px}
  .card-back .holder{margin-top:30px;text-align:center;font-size:6px;font-weight:700;color:var(--brand-navy)}
  .card-back .contact{margin-top:8px;text-align:center;font-size:4px;line-height:6px;color:var(--ink-soft)}
  .card-back .band{position:absolute;left:0;right:0;bottom:0;height:4px;background:var(--brand-green)}

  /* letterhead */
  .letterhead{left:235px;top:10px;width:485px;height:614px;background:var(--brand-green)}
  .letterhead .frame-blue{position:absolute;left:0;top:0;right:10px;bottom:10px;background:var(--brand-blue)}
  .letterhead .sheet{position:absolute;left:10px;top:10px;right:10px;bottom:10px;background:var(--paper)}
  .letterhead .brand-name{position:absolute;left:50%;top:24px;transform:translateX(-50%);font-size:9px;flex-direction:column;text-align:center}
  .letterhead .brand-dot{width:18px;height:18px}
  .letter-body{position:absolute;left:43px;top:142px;width:405px;font-family:"Tinos","Times New Roman",serif;font-size:7px;line-height:9.4px;color:var(--ink)}
  .letter-body .salutation{font-weight:700;font-size:8px;line-height:10px;margin-bottom:20px}
  .letter-body p{margin-bottom:9px;text-align:justify}
  .signature{display:block;width:90px;height:28px;margin-top:4px;background:linear-gradient(90deg,var(--signature-tone),#eeeeee)}
  .letter-footer{position:absolute;left:0;right:0;bottom:6px;text-align:center;font-size:4.5px;color:var(--ink-soft)}

  /* envelope */
  .envelope{left:751px;top:199px;width:432px;height:180px;padding:12px 14px}
  .envelope .brand-name{font-size:7px}
  .envelope .brand-dot{width:12px;height:12px}
  .envelope .return{margin-top:4px;font-size:4.5px;line-height:6px;color:var(--ink-soft)}

  /* compliment slip */
  .slip{left:751px;top:403px;width:432px;height:197px;background:var(--brand-green)}
  .slip .frame-blue{position:absolute;left:0;top:0;right:7px;bottom:7px;background:var(--brand-blue)}
  .slip .sheet{position:absolute;left:7px;top:7px;right:7px;bottom:7px;background:var(--paper);padding:14px 18px}
  .slip .brand-name{font-size:8px}
  .slip .brand-dot{width:14px;height:14px}
  .slip .slip-footer{position:absolute;left:0;right:0;bottom:8px;text-align:center;font-size:4.5px;color:var(--ink-soft)}
</style>
</head>
<body>

<section class="piece card-front" aria-label="Business card front">
  <div class="brand-name"><span class="brand-dot"></span><span>Cellar Guard<br>Sealing</span></div>
</section>

<section class="piece card-back" aria-label="Business card back">
  <div class="brand-name"><span class="brand-dot"></span><span>Cellar Guard<br>Sealing</span></div>
  <div class="holder">Dorian Whitcombe</div>
  <div class="contact">
    4826 Fernhill Glen Court #317 Gainesville, VA 20155<br>
    dwhitcombe@cellarguardsealing.example<br>
    www.cellarguardsealing.example
  </div>
  <div class="band"></div>
</section>

<section class="piece letterhead" aria-label="Letterhead">
  <div class="frame-blue"></div>
  <div class="sheet">
    <div class="brand-name"><span class="brand-dot"></span><span>Cellar Guard<br>Sealing</span></div>
    <div class="letter-body">
      <div class="salutation">Lorem Ipsum<br>dolor sit amet<br>consectetuer adipiscing elit.</div>
      <p>Duis autem vel eum iriure dolor in hendrerit in vulputate velit esse molestie consequat, vel illum dolore eu feugiat nulla facilisis at vero eros et accumsan et iusto odio dignissim qui blandit praesent luptatum zzril delenit augue duis dolore te feugait nulla facilisi. Nam liber tempor cum soluta nobis eleifend option congue nihil imperdiet doming id quod mazim placerat facer possim assum.</p>
      <p>Ut wisi enim ad minim veniam, quis nostrud exerci tation ullamcorper suscipit lobortis nisl ut aliquip ex ea commodo consequat. Typi non habent claritatem insitam; est usus legentis in iis qui facit eorum claritatem. Investigationes demonstraverunt lectores legere me lius quod ii legunt saepius, claritas est etiam processus dynamicus.</p>
      <p>Mirum est notare quam littera gothica, quam nunc putamus parum claram, anteposuerit litterarum formas humanitatis per seacula quarta decima et quinta decima. Eodem modo typi, qui nunc nobis videntur parum clari, fiant sollemnes in futurum. Lorem ipsum dolor sit amet, consectetuer adipiscing elit, sed diam nonummy nibh euismod tincidunt.</p>
      <p>Nam liber tempor cum soluta nobis eleifend option congue nihil imperdiet doming id quod mazim placerat facer possim assum. Duis autem vel eum iriure dolor in hendrerit in vulputate velit esse molestie consequat, vel illum dolore eu feugiat nulla facilisis.</p>
      <p>Sincerely yours,<br>Dorian Whitcombe</p>
      <span class="signature" role="img" aria-label="Handwritten signature"></span>
    </div>
    <div class="letter-footer">4826 Fernhill Glen Court #317 Gainesville, VA 20155 · dwhitcombe@cellarguardsealing.example · www.cellarguardsealing.example</div>
  </div>
</section>

<section class="piece envelope" aria-label="Envelope">
  <div class="brand-name"><span class="brand-dot"></span><span>Cellar Guard<br>Sealing</span></div>
  <div class="return">4826 Fernhill Glen Court #317<br>Gainesville, VA 20155</div>
</section>

<section class="piece slip" aria-label="Compliment slip">
  <div class="frame-blue"></div>
  <div class="sheet">
    <div class="brand-name"><span class="brand-dot"></span><span>Cellar Guard<br>Sealing</span></div>
    <div class="slip-footer">4826 Fernhill Glen Court #317 Gainesville, VA 20155 · www.cellarguardsealing.example</div>
  </div>
</section>

</body>
</html>
```